Web Design for non-profit, Nautical themed

We are developing a web design for a non-profit organization. They are:

a non-profit 501©3 educational and service organization, grounded in the recognition that active engagement of the arts through can be an entry into growth and transformation. Our purpose is to develop and offer events that support this creative process bringing outstanding presenters to our town.

They are located in a beautiful coastal town and the client would like a "nautical" theme. This would include

- color palette of blue, green, possibly brown/beige, and possibly some deep red colors as accents. There is a file attached with some color palette ideas, but you don't have to choose from colors here.

- soothing, calm, clean professional look

- something in the background image that would indicate the four directions. This could be a compass or something similar.

- the client really likes this website:
http://www.thelarkmoorcenter.org/

Please see attached for:

- a basic sketch that shows the overall layout that we desire. Feel free to modify this slightly but not too much. File name is 01-sketch.psd

- placeholder content that can be used throughout your design

You can also use any of the stock photos found here:
http://www.pixvaultimages.com/search/lightbox/48207356#a9d1b72

Target Market(s)

Mainly white American women who are in their 40s or older. Professional, affluent, highly educated.

Industry/Entity Type

Nautical

Requirements
Must have
• - sidebar with event information. Each event should include date, headshot, title, brief description and a "Register" and "Read more" link. We don't have any real headshots so use ones from Internet for now.

- use the attached 01-sketch.psd file as your starting point.

```html
<!DOCTYPE html>
<html lang="en">
<head>
<meta charset="utf-8">
<title>Harborlight Dialogues Inc.</title>
<link rel="stylesheet" href="https://fonts.googleapis.com/css2?family=Oswald:wght@400&family=Ubuntu:wght@400;500&display=swap">
<style>
:root{
  --navy:#1d4f9a;
  --navy-dark:#163f7e;
  --nav-top:#3d7cc9;
  --nav-bottom:#1a4f99;
  --panel-blue:#2358a6;
  --text:#4a4a4a;
  --heading:#1f4f93;
  --card-border:#dcdcdc;
  --footer-top:#7a7a7a;
  --footer-bottom:#565656;
  --white:#ffffff;
}
*{box-sizing:border-box;margin:0;padding:0}
html,body{width:1200px;height:1055px;overflow:hidden;background:var(--white)}
body{position:relative;font-family:"Ubuntu",sans-serif;color:var(--text)}
.abs{position:absolute}
.brand{left:160px;top:22px;width:220px;height:70px;display:flex;align-items:center;gap:8px;color:#333;line-height:1}
.brand-mark{width:30px;height:30px;border-radius:50%;background:#333;flex:none}
.brand-name{font-size:23px;line-height:1.05}
.main-nav{left:388px;top:50px;width:654px;height:35px;display:flex;border-radius:3px;background:linear-gradient(var(--nav-top),var(--nav-bottom));box-shadow:0 2px 3px rgba(0,0,0,.3)}
.main-nav a{font-family:"Oswald",sans-serif;font-size:13px;color:var(--white);text-decoration:none;display:flex;align-items:center;justify-content:center;border-right:1px solid #164383;text-transform:uppercase}
.main-nav a:last-child{border-right:none}
.signup{left:160px;top:104px;width:231px;height:121px;background:linear-gradient(#7a7a7a,#5c5c5c);border-radius:3px;box-shadow:0 1px 3px rgba(0,0,0,.4)}
.social-row{position:absolute;left:15px;top:17px;display:flex;gap:10px}
.social-row span{width:27px;height:27px;border-radius:4px;background:#3f74c4;display:block}
.social-row span:nth-child(2){background:#5aaee3}
.social-row span:nth-child(3){background:#d8d8d8}
.signup h3{position:absolute;left:15px;top:58px;font-family:"Oswald",sans-serif;font-weight:400;font-size:13px;color:var(--white)}
.signup .field{position:absolute;left:15px;top:82px;width:157px;height:26px;background:var(--white);border-radius:2px}
.signup .join{position:absolute;left:177px;top:82px;width:47px;height:26px;background:#2d8fcf;color:var(--white);font-family:"Oswald",sans-serif;font-size:13px;display:flex;align-items:center;justify-content:center;border-radius:2px}
.events{left:160px;top:236px;width:231px;height:592px;background:var(--panel-blue);border-radius:3px;box-shadow:0 1px 3px rgba(0,0,0,.4);color:var(--white)}
.events h2{position:absolute;left:14px;top:12px;font-family:"Oswald",sans-serif;font-weight:400;font-size:17px}
.event{position:absolute;left:0;width:231px}
.headshot{position:absolute;left:14px;top:0;width:58px;height:75px;border:2px solid #e8e8e8}
.event h4{position:absolute;left:82px;top:-3px;font-size:13.5px;font-weight:500;line-height:19px;white-space:nowrap}
.event .date{position:absolute;left:82px;top:40px;font-size:10.5px;color:#c9d8f0}
.event .who{position:absolute;left:82px;top:57px;font-size:10.5px;font-weight:500}
.event p{position:absolute;left:84px;top:84px;width:133px;font-size:11.5px;line-height:18.5px;text-align:justify;hyphens:auto;-webkit-hyphens:auto}
.btn{position:absolute;top:208px;height:28px;background:linear-gradient(#fafafa,#dcdcdc);border-radius:3px;color:var(--navy);font-size:11.5px;display:flex;align-items:center;gap:5px;padding:0 8px;box-shadow:0 1px 2px rgba(0,0,0,.4)}
.btn.register{left:18px;width:75px}
.btn.more{left:101px;width:90px}
.ico{width:11px;height:11px;flex:none}
.divider{position:absolute;left:0;top:260px;width:231px;height:1px;background:#1a4a8f;box-shadow:0 1px 0 #3a6fbd}
.slider{left:410px;top:101px;width:632px;height:397px;background:linear-gradient(#4b56b8 0%,#5a64c4 45%,#5d5560 75%,#3a3840 100%)}
.arrow{width:44px;height:44px;border-radius:50%;background:#3a3a3a;border:3px solid #e6e6e6;display:flex;align-items:center;justify-content:center;box-shadow:0 1px 3px rgba(0,0,0,.4)}
.intro{left:410px;top:504px;width:632px;height:80px;background:linear-gradient(#f2f2f2,#ffffff 40%)}
.intro h1{position:absolute;left:16px;top:15px;font-size:17px;font-weight:400;color:var(--heading)}
.intro p{position:absolute;left:16px;top:42px;width:595px;font-size:12.3px;line-height:19px}
.card{top:601px;height:228px;border:1px solid var(--card-border);border-radius:3px;background:linear-gradient(#f6f6f6,#ffffff 30%)}
.card h3{position:absolute;left:13px;top:10px;font-size:17px;font-weight:400;color:var(--heading)}
.card p{position:absolute;left:13px;top:35px;width:176px;font-size:12.5px;line-height:20.3px;text-align:justify;hyphens:auto;-webkit-hyphens:auto}
.card .more-link{position:absolute;left:13px;top:205px;height:21px;padding:0 9px;background:var(--navy-dark);color:var(--white);font-size:11px;display:flex;align-items:center;border-radius:2px}
.site-footer{left:0;top:853px;width:1200px;height:202px;background:linear-gradient(var(--footer-top),var(--footer-bottom));color:var(--white)}
.site-footer h4{position:absolute;top:14px;font-size:15px;font-weight:400}
.site-footer ul{position:absolute;list-style:none;font-size:11px;line-height:24px}
.site-footer .line{position:absolute;font-size:11px}
.follow{position:absolute;left:933px;top:49px;display:flex;gap:8px}
.follow span{width:21px;height:21px;border-radius:3px;background:#3f74c4;display:block}
.follow span:nth-child(2){background:#44a6e0}
.follow span:nth-child(3){background:#1f6db3}
.follow span:nth-child(4){background:#f08a1c}
</style>
</head>
<body>

<header>
  <div class="abs brand"><span class="brand-mark"></span><span class="brand-name">Harborlight Dialogues Inc.</span></div>
  <nav class="abs main-nav">
    <a href="#" style="width:89px">Home</a>
    <a href="#" style="width:103px">Calendar</a>
    <a href="#" style="width:103px">About Us</a>
    <a href="#" style="width:100px">Donate</a>
    <a href="#" style="width:138px">Travel Information</a>
    <a href="#" style="width:121px">Contact Us</a>
  </nav>
</header>

<aside>
  <section class="abs signup">
    <div class="social-row"><span></span><span></span><span></span></div>
    <h3>JOIN OUR MAILING LIST</h3>
    <div class="field"></div>
    <div class="join">JOIN</div>
  </section>

  <section class="abs events">
    <h2>UPCOMING EVENTS</h2>

    <article class="event" style="top:50px">
      <div class="headshot" role="img" aria-label="Presenter headshot" style="background:linear-gradient(#e8c98a,#c79a5e)"></div>
      <h4>Starting Close In<br>Presenters</h4>
      <div class="date">May 28, 2013</div>
      <div class="who">Daniel and Ruth Marlowe</div>
      <p>Heeding the implicit wisdom in R.M. Ellery's line "We had the experience but missed the meaning," this concluding workshop is ..</p>
      <div class="btn register"><svg class="ico" viewBox="0 0 12 12"><circle cx="6" cy="3.5" r="2.8" fill="#1d4f9a"/><path d="M1 12c0-3.5 2.2-5 5-5s5 1.5 5 5z" fill="#1d4f9a"/></svg>Register</div>
      <div class="btn more">Read More <svg class="ico" viewBox="0 0 12 12"><rect x=".5" y=".5" width="11" height="11" rx="2" fill="#999"/><path d="M6 3v6M3 6h6" stroke="#fff" stroke-width="1.5"/></svg></div>
      <div class="divider"></div>
    </article>

    <article class="event" style="top:331px">
      <div class="headshot" role="img" aria-label="Presenter headshot" style="background:linear-gradient(#b88a6a,#6d4a3a)"></div>
      <h4>A Journey of Discovery<br>Along the Chesapeake..</h4>
      <div class="date">May 28, 2013</div>
      <div class="who">Owen Talbridge, PhD</div>
      <p>Join local naturalist and marine biologist Owen Talbridge, PhD on an invigorating and rejuvenating morning nature walk amidst.</p>
      <div class="btn register"><svg class="ico" viewBox="0 0 12 12"><circle cx="6" cy="3.5" r="2.8" fill="#1d4f9a"/><path d="M1 12c0-3.5 2.2-5 5-5s5 1.5 5 5z" fill="#1d4f9a"/></svg>Register</div>
      <div class="btn more">Read More <svg class="ico" viewBox="0 0 12 12"><rect x=".5" y=".5" width="11" height="11" rx="2" fill="#999"/><path d="M6 3v6M3 6h6" stroke="#fff" stroke-width="1.5"/></svg></div>
    </article>
  </section>
</aside>

<main>
  <div class="abs slider" role="img" aria-label="Evening street scene of a historic harbor town with a domed state house"></div>
  <div class="abs arrow" style="left:401px;top:277px"><svg width="14" height="18" viewBox="0 0 14 18"><path d="M10 2 3 9l7 7" fill="none" stroke="#fff" stroke-width="2.5"/></svg></div>
  <div class="abs arrow" style="left:1010px;top:277px"><svg width="14" height="18" viewBox="0 0 14 18"><path d="m4 2 7 7-7 7" fill="none" stroke="#fff" stroke-width="2.5"/></svg></div>

  <section class="abs intro">
    <h1>Conversations that could transform your life</h1>
    <p>Harborlight Dialogues is bringing together speakers from around the globe who are transforming our world. change to us for event that cloud change your life.</p>
  </section>

  <section class="abs card" style="left:413px;width:202px">
    <h3>About Us</h3>
    <p>Harborlight Dialogues Inc. is a non-profit 501©3 educational and service organization, grounded in the recognition that active engagement of the arts through can be an entry into growth and transformation</p>
    <div class="more-link">Read More</div>
  </section>
  <section class="abs card" style="left:626px;width:202px">
    <h3>Our Speakers</h3>
    <p>Harborlight Dialogues, Inc. is an organization of volunteers. We have no walls. We utilize a wide range of resources in selecting appropriate venues and personnel.Our home area is the greater Bayhaven harbor region....</p>
    <div class="more-link">Read More</div>
  </section>
  <section class="abs card" style="left:841px;width:201px">
    <h3>How you can help</h3>
    <p>Harborlight Dialogues Inc. is a non-profit 501©3 educational and service organization, grounded in the recognition that active engagement of the arts through can be an entry into growth and transformation</p>
    <div class="more-link">Read More</div>
  </section>
</main>

<footer class="abs site-footer">
  <h4 style="left:160px">Site Map</h4>
  <ul style="left:161px;top:35px">
    <li>Home</li><li>Calendar</li><li>About Us</li><li>Donate</li><li>Travel Information</li><li>Contact us</li>
  </ul>
  <h4 style="left:383px">Contact Us</h4>
  <div class="line" style="left:384px;top:40px">PO Box 4417, Bayhaven, MD 21409.</div>
  <div class="line" style="left:384px;top:64px">E mail</div>
  <div class="line" style="left:384px;top:88px">to info@harborlightdialogues.org</div>
  <h4 style="left:954px">Follow us On</h4>
  <div class="follow"><span></span><span></span><span></span><span></span></div>
  <div class="line" style="left:825px;top:88px">©2013 educational and service organization</div>
</footer>

</body>
</html>
```